Homepage web design

I need a homepage design that will be easy to build into a default Word Press theme. Basically, header, navigation, body with sidebar, and footer.

This website is for a small commercial real estate firm in the Washington DC, Maryland and Virginia market.

THIS IS NOT A HOUSING/RESIDENTIAL WEBSITE. PLEASE DO NOT ADD ANY PROPERTY SEARCH FUNCTIONALITY.

Target Market(s)

People looking for basic information about the team and services provided.

Industry/Entity Type

Real Estate

Requirements
Must have
• Professional look. Clean design.

```html
<!DOCTYPE html>
<html lang="en">
<head>
<meta charset="utf-8">
<title>Meridian Commercial Brokerage</title>
<link rel="stylesheet" href="https://fonts.googleapis.com/css2?family=Cuprum:wght@400;700&family=Arimo&display=swap">
<style>
  :root{
    --green:#0b8a4f;
    --sample:#8fc7b0;
    --line:#b9ddcd;
    --text:#333333;
    --dot:#d6d6d6;
    --paper:#f5f5f3;
  }
  *{box-sizing:border-box;margin:0;padding:0}
  html,body{width:780px;height:1200px;overflow:hidden;background:var(--paper)}
  body{position:relative;font-family:"Cuprum",sans-serif;color:var(--text)}
  .page{position:relative;width:780px;height:1200px}
  a{color:inherit;text-decoration:none}

  .brand{position:absolute;top:110px;left:0;width:780px;display:flex;justify-content:center;align-items:center;gap:12px}
  .brand-mark{width:22px;height:22px;background:var(--green)}
  .brand-name{font-size:34px;font-weight:700;color:var(--green);letter-spacing:.5px}

  .main-nav{position:absolute;top:211px;left:15px;width:749px;height:54px;border-top:1px solid var(--green);border-bottom:1px solid var(--green);
    display:flex;align-items:center;justify-content:space-between;padding:0 24px}
  .main-nav a{font-size:19px;letter-spacing:.5px;text-transform:uppercase;color:#3a3a3a}
  .nav-dot{width:9px;height:9px;border-radius:50%;background:#9a9a9a}

  .slider{position:absolute;top:281px;left:15px;width:749px;height:271px;border:1px solid var(--line)}
  .sample-fill{background:var(--sample);display:flex;align-items:center;justify-content:center;color:#fff;font-size:34px;letter-spacing:1px}
  .slider .sample-fill{position:absolute;left:15px;top:15px;width:375px;height:243px;font-size:38px}
  .slide-copy{position:absolute;left:408px;top:24px;width:330px}
  .slide-title{font-size:21px;color:var(--green);font-weight:400}
  .slide-price{font-family:"Arimo",sans-serif;font-size:22px;color:#555;margin-top:6px}
  .slide-text{font-size:13px;line-height:18px;margin-top:46px}
  .btn{display:inline-flex;align-items:center;justify-content:center;background:var(--green);color:#fff;font-size:17px;font-weight:700;width:123px;height:29px}
  .slide-copy .btn{margin-top:26px}
  .slider-dots{display:flex;gap:7px;margin-top:16px}
  .slider-dots span{width:16px;height:16px;border-radius:50%;background:var(--dot)}
  .slider-dots .active{background:var(--sample)}

  .section-title{font-size:22px;color:var(--green);text-transform:uppercase;letter-spacing:.5px;font-weight:400}
  .proposals{position:absolute;top:564px;left:15px;width:749px}
  .proposals .section-title{border-bottom:1px solid var(--line);padding-bottom:4px}
  .cards{display:flex;justify-content:space-between;margin-top:9px}
  .card{width:177px;height:232px;border:1px solid var(--line);padding:14px}
  .card .sample-fill{height:126px;font-size:28px}
  .card-lead{color:var(--green);font-size:13.5px;line-height:19px;margin-top:6px}
  .card-text{font-size:12.5px;line-height:17px;margin-top:4px}

  .info{position:absolute;top:843px;left:15px;width:749px;display:flex;justify-content:space-between}
  .info-col{width:235px}
  .info-col .section-title{font-size:21px;line-height:26px;border-bottom:1px solid var(--line);padding-bottom:4px}
  .info-sub{font-size:16px;line-height:22px;font-weight:400;margin-top:8px;letter-spacing:.4px;white-space:nowrap}
  .info-text{font-size:12.5px;line-height:18px;margin-top:9px;text-align:justify;height:72px;overflow:hidden}
  .info-col .btn{margin-top:8px}

  .site-footer{position:absolute;top:1037px;left:15px;width:749px;border-top:1px solid var(--line)}
  .footer-cols{position:relative;height:134px}
  .footer-col{position:absolute;top:12px}
  .footer-col h3{font-size:17px;color:var(--green);font-weight:700;text-transform:uppercase;margin-bottom:3px}
  .footer-col li{list-style:none;font-size:14px;line-height:22.5px}
  .footer-bar{border-top:1px solid var(--line);display:flex;justify-content:space-between;font-size:10px;padding-top:9px;color:#222}
  .footer-contact{display:flex;gap:26px}
  .footer-phone{margin-right:50px}
</style>
</head>
<body>
<div class="page">
  <header class="brand">
    <span class="brand-mark"></span>
    <span class="brand-name">Meridian Commercial Brokerage</span>
  </header>

  <nav class="main-nav">
    <a href="#">Home</a><span class="nav-dot"></span>
    <a href="#">About</a><span class="nav-dot"></span>
    <a href="#">Building</a><span class="nav-dot"></span>
    <a href="#">Moving</a><span class="nav-dot"></span>
    <a href="#">Selling</a><span class="nav-dot"></span>
    <a href="#">Contact</a>
  </nav>

  <section class="slider">
    <div class="sample-fill" role="img" aria-label="Featured commercial property photo">SAMPLE</div>
    <div class="slide-copy">
      <h2 class="slide-title">SAMPLE</h2>
      <p class="slide-price">$VALUE</p>
      <p class="slide-text">Lorem ipsum dolor sit amet, consec-tetur adipisicing elit, sed do eiusmod tempor incididunt ut labore et dolore</p>
      <a class="btn" href="#">Read more</a>
      <div class="slider-dots"><span></span><span class="active"></span><span></span><span></span></div>
    </div>
  </section>

  <section class="proposals">
    <h2 class="section-title">Best Proposals</h2>
    <div class="cards">
      <article class="card">
        <div class="sample-fill" role="img" aria-label="Property photo">SAMPLE</div>
        <p class="card-lead">Lorem ipsum dolor sit amet, consectetur adipisicing.</p>
        <p class="card-text">Lorem ipsum dolor sit amet, consectetur adipisicing.</p>
      </article>
      <article class="card">
        <div class="sample-fill" role="img" aria-label="Property photo">SAMPLE</div>
        <p class="card-lead">Lorem ipsum dolor sit amet, consectetur adipisicing.</p>
        <p class="card-text">Lorem ipsum dolor sit amet, consectetur adipisicing.</p>
      </article>
      <article class="card">
        <div class="sample-fill" role="img" aria-label="Property photo">SAMPLE</div>
        <p class="card-lead">Lorem ipsum dolor sit amet, consectetur adipisicing.</p>
        <p class="card-text">Lorem ipsum dolor sit amet, consectetur adipisicing.</p>
      </article>
      <article class="card">
        <div class="sample-fill" role="img" aria-label="Property photo">SAMPLE</div>
        <p class="card-lead">Lorem ipsum dolor sit amet, consectetur adipisicing.</p>
        <p class="card-text">Lorem ipsum dolor sit amet, consectetur adipisicing.</p>
      </article>
    </div>
  </section>

  <section class="info">
    <div class="info-col">
      <h2 class="section-title">About Us</h2>
      <h3 class="info-sub">Duis ac turpis. Integer rutrum ante</h3>
      <p class="info-text">Lorem ipsum dolor sit amet, consectetur adipisicing elit, sed do eiusmod tempor incididunt ut labore et dolore magna aliqua. Ut enim ad minim veniam, quis nostrud.</p>
      <a class="btn" href="#">Read more</a>
    </div>
    <div class="info-col">
      <h2 class="section-title">Our Services</h2>
      <h3 class="info-sub">Duis ac turpis. Integer rutrum ante</h3>
      <p class="info-text">Lorem ipsum dolor sit amet, consectetur adipisicing elit, sed do eiusmod tempor incididunt ut labore et dolore magna aliqua. Ut enim ad minim veniam, quis nostrud.</p>
      <a class="btn" href="#">Read more</a>
    </div>
    <div class="info-col">
      <h2 class="section-title">Contact</h2>
      <h3 class="info-sub">Duis ac turpis. Integer rutrum ante</h3>
      <p class="info-text">Lorem ipsum dolor sit amet, consectetur adipisicing elit, sed do eiusmod tempor incididunt ut labore et dolore magna aliqua. Ut enim ad minim veniam, quis nostrud.</p>
      <a class="btn" href="#">Read more</a>
    </div>
  </section>

  <footer class="site-footer">
    <div class="footer-cols">
      <div class="footer-col" style="left:0">
        <h3>Company</h3>
        <ul><li>About us</li><li>Services</li><li>Presentation</li><li>Clients</li></ul>
      </div>
      <div class="footer-col" style="left:194px">
        <h3>Porperties</h3>
        <ul><li>Commercial</li><li>Residential</li><li>Luxury</li></ul>
      </div>
      <div class="footer-col" style="left:382px">
        <h3>Advice</h3>
        <ul><li>FAQs</li><li>Support</li></ul>
      </div>
      <div class="footer-col" style="left:557px">
        <h3>Clients</h3>
        <ul><li>Sign up</li><li>Forums</li><li>Presentation</li><li>Promotions</li></ul>
      </div>
    </div>
    <div class="footer-bar">
      <span>Meridian Commercial Brokerage ©</span>
      <div class="footer-contact">
        <span class="footer-phone">Telephone : 000-000-0000</span>
        <span>Fax: 000-000-0000</span>
        <span>Email: hello@meridiancb.test</span>
      </div>
    </div>
  </footer>
</div>
</body>
</html>
```